New high end server provider needs wordpress design

www.kv7hosting.com

Need a wordpress design for a high end server provider that provides overclocked dedicated servers for rent. We are located in Chicago but we have a presence is Virginia and Nevada for both our east and west coast customers.

We are a server provider that specializes in top end hardware with every feature designed for optimum performance. If it is not the best quality part or provides the best possible performance we don't run it. Our customers are mainly those that want the best single threaded performance possible from their hardware. We would be selling our services directly on our website via WHMCS.

We would like to see designs that are very modern and simplistic yet very attractive looking and catchy. Would prefer colors in the blues and greens and white. These colors are not necessary and I would be open to another color scheme if it looks good.

The final design should show speed and performance while being simplistic and easy on the eyes.

Logo and company name added and payment changed to guaranteed.  Looking for a wordpress template with the same pages as kv7hosting.com but with a redesigned look and feel.  

WHMCS control panel design also part of the design request.

If you have any questions please let me know!  This is just for kv7hosting.com and a main page for WHMCS (no coding just design).

Target Market(s)

IT Guru's (mostly men in their 20's to 30's)

Industry/Entity Type

Hardware

Requirements
Must have
• WHMCS panel design to fit with website theme.
Nice to have
• Main slider on home page similar to one of our other websites at www.kv7hosting.com
Should not have
• Flash or frames

```html
<!DOCTYPE html>
<html lang="en">
<head>
<meta charset="utf-8">
<title>KV7 Hosting – Client Area Login</title>
<link href="https://fonts.googleapis.com/css2?family=Arimo:wght@400;700&family=Tinos:wght@700&display=swap" rel="stylesheet">
<style>
  :root{
    --page-grey:#d9d9d9;
    --band-blue:#1a73d4;
    --band-blue-dark:#0a4ea8;
    --footer-blue:#0a4593;
    --footer-line:#2a5ea6;
    --panel-white:#ffffff;
    --nav-text:#555555;
    --subnav-dark:#2c2c2c;
    --subnav-text:#a8a8a8;
    --ink:#333333;
    --link-orange:#f07800;
    --button-blue:#1565c8;
    --partner-grey:#4a4a4a;
    --footer-text:#9fb9de;
  }
  *{box-sizing:border-box;margin:0;padding:0}
  html,body{width:1200px;height:839px;overflow:hidden}
  body{position:relative;background:var(--page-grey);font-family:"Arimo",Arial,sans-serif;color:var(--ink)}
  .abs{position:absolute}

  .top-shade{left:0;top:0;width:1200px;height:14px;background:linear-gradient(#c4c4c4,var(--page-grey))}
  .logo{left:254px;top:24px;font-family:"Tinos",Georgia,serif;font-weight:700;font-size:29px;color:#4a4a4a;letter-spacing:1px}

  .hero-band{left:0;top:102px;width:1200px;height:56px;
    background:linear-gradient(#5aa6f0 0%,var(--band-blue) 35%,var(--band-blue-dark) 100%);
    box-shadow:0 3px 5px rgba(0,0,0,.25)}
  .main-nav{left:247px;top:79px;width:707px;height:31px;border-radius:9px;
    background:linear-gradient(#ffffff,#e6e6e6);box-shadow:0 1px 3px rgba(0,0,0,.25);
    display:flex;align-items:center;padding-left:42px}
  .main-nav a{font-family:"Tinos",Georgia,serif;font-weight:700;font-size:12px;color:var(--nav-text);
    text-decoration:none;text-transform:uppercase;height:31px;line-height:31px;padding:0 6px}
  .main-nav a.active{background:linear-gradient(#cfcfcf,#b9b9b9);color:#222}

  .server-icon{left:262px;top:125px;width:34px;height:49px;border-radius:3px;
    background:linear-gradient(90deg,#111,#4a4a4a 60%,#222)}
  .page-title{left:308px;top:133px;font-size:17px;font-weight:700;color:#fff}

  .footer-band{left:0;top:688px;width:1200px;height:151px;background:var(--footer-blue)}
  .panel{left:247px;top:190px;width:707px;height:543px;background:var(--panel-white);box-shadow:0 0 4px rgba(0,0,0,.2)}

  .sub-nav{left:269px;top:203px;width:674px;height:30px;border-radius:3px;
    background:linear-gradient(#444,var(--subnav-dark));display:flex;align-items:center;padding-left:22px}
  .sub-nav a{font-size:10px;font-weight:700;color:var(--subnav-text);text-decoration:none;margin-right:23px}
  .sub-nav .account{margin-left:auto;margin-right:22px}
  .sub-nav .account::after{content:"";display:inline-block;margin-left:5px;vertical-align:middle;
    border:3px solid transparent;border-top-color:var(--subnav-text)}

  .login-title{left:439px;top:264px;font-size:24px;font-weight:700;letter-spacing:-1px;color:#222}
  .rule{left:439px;top:305px;width:333px;height:1px;background:#e2e2e2}
  .label{font-size:11px;font-weight:700;color:#333}
  .field{width:210px;height:21px;border:1px solid #bdbdbd;background:#fff;box-shadow:inset 0 1px 2px rgba(0,0,0,.08)}
  .btn-login{left:534px;top:432px;width:47px;height:28px;border-radius:3px;
    background:linear-gradient(#3a8be0,var(--button-blue));color:#fff;font-size:11px;text-align:center;line-height:28px}
  .remember{left:600px;top:439px;font-size:10px;font-weight:700;display:flex;align-items:center;gap:6px}
  .remember i{width:10px;height:10px;border:1px solid #999;background:#f4f4f4;display:block}
  .reset-link{left:506px;width:200px;top:473px;text-align:center;font-size:10px;color:var(--link-orange)}
  .powered{left:456px;width:300px;top:565px;text-align:center;font-size:10px;color:#333}
  .powered span{color:var(--link-orange)}

  .language{left:271px;top:605px;font-size:9px;font-weight:700;color:#444}
  .lang-select{left:320px;top:604px;width:77px;height:17px;border:1px solid #aaa;border-radius:3px;
    font-size:9px;line-height:15px;padding-left:6px;color:#444;background:#fff}
  .lang-select b{position:absolute;right:3px;top:2px;width:11px;height:11px;border:1px solid #777;background:#eee}
  .lang-select b::after{content:"";position:absolute;left:2px;top:3px;border:3px solid transparent;border-top-color:#333}

  .partner-rule{left:269px;top:679px;width:674px;height:1px;background:#e5e5e5}
  .partner{top:696px;height:24px;background:var(--partner-grey);border-radius:3px}

  .footer-links{left:253px;top:756px;font-size:8.5px;line-height:15px;color:var(--footer-text)}
  .social{top:751px;width:34px;height:34px;border-radius:4px;border:1px solid #6d8fbf;
    background:linear-gradient(#3e6aa8,#163f78);box-shadow:0 1px 3px rgba(0,0,0,.4)}
  .footer-rule{left:0;top:800px;width:1200px;height:1px;background:var(--footer-line)}
  .copyright{left:0;width:1200px;top:817px;text-align:center;font-size:8.5px;color:var(--footer-text)}
</style>
</head>
<body>
  <div class="abs top-shade"></div>
  <div class="abs logo">LOGO</div>

  <div class="abs hero-band"></div>
  <nav class="abs main-nav">
    <a>Home</a><a style="margin-left:16px">Our Servers</a><a class="active" style="margin-left:16px">Client Area</a>
    <a style="margin-left:29px">Why Us?</a><a style="margin-left:29px">Testimonials</a><a style="margin-left:22px">Contacts</a>
  </nav>
  <div class="abs server-icon" role="img" aria-label="Server tower icon"></div>
  <h1 class="abs page-title">Client Area</h1>

  <div class="abs footer-band"></div>
  <main class="abs panel"></main>

  <nav class="abs sub-nav">
    <a>Home</a><a>Announcements</a><a>Knowledgebase</a><a>Network Status</a><a>Affiliates</a><a>Contact Us</a>
    <a class="account">Account</a>
  </nav>

  <h2 class="abs login-title">Login</h2>
  <div class="abs rule"></div>
  <div class="abs label" style="left:500px;top:329px">Email Address:</div>
  <div class="abs field" style="left:500px;top:346px"></div>
  <div class="abs label" style="left:500px;top:381px">Password:</div>
  <div class="abs field" style="left:500px;top:397px"></div>
  <div class="abs btn-login">Login</div>
  <div class="abs remember"><i></i>Remember Me</div>
  <div class="abs reset-link">Request a Password Reset</div>
  <div class="abs powered">Powered by <span>HostDeskSuite</span></div>

  <div class="abs language">Language:</div>
  <div class="abs lang-select">English<b></b></div>

  <div class="abs partner-rule"></div>
  <div class="abs partner" style="left:271px;width:118px" role="img" aria-label="Partner badge"></div>
  <div class="abs partner" style="left:427px;width:22px" role="img" aria-label="Partner badge"></div>
  <div class="abs partner" style="left:485px;width:40px" role="img" aria-label="Partner badge"></div>
  <div class="abs partner" style="left:553px;width:22px" role="img" aria-label="Partner badge"></div>
  <div class="abs partner" style="left:617px;width:96px" role="img" aria-label="Partner badge"></div>

  <div class="abs footer-links">
    Home | Our Servers | Client Area | Why Us? | Testimonials | Contact<br>
    Privacy Policy | Terms of use
  </div>
  <div class="abs social" style="left:774px" role="img" aria-label="Social link"></div>
  <div class="abs social" style="left:822px" role="img" aria-label="Social link"></div>
  <div class="abs social" style="left:870px" role="img" aria-label="Social link"></div>
  <div class="abs social" style="left:918px" role="img" aria-label="Social link"></div>
  <div class="abs footer-rule"></div>
  <div class="abs copyright">Copyright 2013. All Rights Reserved.</div>
</body>
</html>
```